Marlow Creek Stud website

We would like to create a horse stud/agistment farm website similar to this websites we have attached below:
www.hollistead.com.au
www.quandrell.com.au
www.barrowick.com
www.fenshaw.com.au
The main colour scheme are purple and white to align with the stable's racing colours.
We have also attach the company logo and also images of the farm and create some ideas for the website.
Many thanks for looking into this project!

```html
<!DOCTYPE html>
<html lang="en">
<head>
<meta charset="utf-8">
<title>Marlow Creek Stud</title>
<link href="https://fonts.googleapis.com/css2?family=Cinzel:wght@400;500&family=Lato:ital,wght@0,400;0,700;1,400&display=swap" rel="stylesheet">
<style>
:root{
  --purple:#45193f;
  --purple-deep:#3a1436;
  --purple-night:#2c0d29;
  --ink:#3b3b3b;
  --muted:#6d6d6d;
  --line:#d6d6d6;
  --white:#ffffff;
  --serif:'Cinzel', 'Times New Roman', serif;
  --sans:'Lato', Arial, sans-serif;
}
*{margin:0;padding:0;box-sizing:border-box}
html,body{width:1200px;height:4054px;overflow:hidden}
body{position:relative;background:var(--white);font-family:var(--sans);color:var(--ink)}
.abs{position:absolute}
.photo{position:absolute}

/* top bar */
.top-bar{left:0;top:0;width:1200px;height:43px;background:var(--purple-deep);color:var(--white);font-size:15px}
.top-bar .item{position:absolute;top:12px;display:flex;align-items:center;gap:10px}

/* nav */
.site-nav{left:0;top:43px;width:1200px;height:92px;background:var(--white)}
.brand{position:absolute;left:81px;top:30px;display:flex;align-items:center;gap:12px;font-family:var(--sans);font-weight:700;font-size:24px;color:var(--purple)}
.brand .dot{width:30px;height:30px;border-radius:50%;background:var(--purple)}
.menu{position:absolute;right:78px;top:37px;display:flex;gap:29px;font-size:15px;color:#555;letter-spacing:.5px}
.menu .active{color:var(--purple);border-bottom:2px solid var(--purple);padding-bottom:14px}

/* hero */
.hero-photo{left:0;top:135px;width:1200px;height:555px;background:linear-gradient(180deg,#5d6a3c 0%,#7c8a43 40%,#b6b23a 75%,#c7bf45 100%)}
.hero-disc{left:89px;top:230px;width:378px;height:378px;border-radius:50%;background:var(--purple)}
.hero-title{left:89px;top:355px;width:378px;text-align:center;font-family:var(--serif);font-size:35px;line-height:42px;color:var(--white)}
.hero-arrow{left:410px;top:486px}

/* section titles */
.section-title{width:1200px;left:0;text-align:center;font-family:var(--serif);font-size:42px;color:var(--purple-deep);letter-spacing:1px}

/* stallions */
.stallion-card .photo{width:322px;height:260px}
.stallion-name{font-size:18px;color:#555}
.round-arrow{width:32px;height:32px}
.slider-line{left:78px;top:1257px;width:1044px;height:1px;background:var(--line)}
.slider-nav{left:532px;top:1238px;display:flex;gap:12px}
.slider-nav span{width:60px;height:38px;border:1px solid #bbb;border-radius:19px;background:var(--white);display:flex;align-items:center;justify-content:center}
.intro-quote{left:0;top:1342px;width:1200px;text-align:center;font-style:italic;font-size:21px;line-height:33px;color:#555}

/* news */
.news-photo{left:0;top:1484px;width:522px;height:481px;background:linear-gradient(135deg,#2a2a2a 0%,#8b6a3e 40%,#c9a468 70%,#9fa46a 100%)}
.news-title{left:608px;top:1550px;font-family:var(--serif);font-size:42px;color:var(--purple-deep)}
.news-lead{left:608px;top:1612px;width:480px;font-size:20px;line-height:28px;color:#5b4a58}
.news-body{left:608px;top:1710px;width:486px;font-size:14.5px;line-height:24px;color:#666}

/* banner */
.banner{left:78px;top:2054px;width:1044px;height:373px;background:linear-gradient(90deg,#2d2a24 0%,#4a3a2c 45%,#3a3428 100%)}
.banner-text{left:78px;top:2190px;width:1044px;text-align:center;font-family:var(--serif);font-size:34px;line-height:44px;color:var(--white)}

/* gallery */
.gallery .photo{width:333px;height:260px}

/* landscape */
.landscape{left:0;top:3135px;width:1200px;height:473px;background:linear-gradient(180deg,#c8d5e0 0%,#9fb1bd 25%,#6d8a5c 50%,#a9bb7a 75%,#dfe4d5 100%)}

/* footer */
.footer{left:0;top:3608px;width:1200px;height:382px;background:var(--purple)}
.subscribe{left:311px;top:3562px;width:581px;height:82px;border-radius:41px;background:var(--white);display:flex;align-items:center;justify-content:space-between;padding:0 45px 0 48px;font-style:italic;font-size:17px;color:#999}
.subscribe-title{left:0;top:3694px;width:1200px;text-align:center;font-family:var(--serif);font-size:25px;color:var(--white);letter-spacing:1px}
.footer-brand{left:81px;top:3782px;display:flex;align-items:center;gap:10px;font-weight:700;font-size:22px;color:var(--white)}
.footer-brand .dot{width:26px;height:26px;border-radius:50%;background:var(--white)}
.footer-about{left:81px;top:3874px;width:290px;font-size:15px;line-height:26px;color:#e7dbe5}
.footer-heading{font-family:var(--serif);font-size:21px;color:var(--white);letter-spacing:1px;top:3754px}
.sitemap{list-style:none;font-size:15px;color:var(--white)}
.sitemap li{height:38px;display:flex;align-items:center;gap:16px}
.sitemap li::before{content:"";width:9px;height:9px;border-radius:50%;background:var(--white)}
.contact-row{left:800px;display:flex;gap:16px;font-size:15px;line-height:24px;color:var(--white);width:300px}
.contact-row svg{flex:none;margin-top:3px}
.copyright{left:0;top:3990px;width:1200px;height:64px;background:var(--purple-night);text-align:center;line-height:64px;font-size:15px;color:#e7dbe5}
</style>
</head>
<body>

<header class="abs top-bar">
  <div class="item" style="left:766px">
    <svg width="16" height="16" viewBox="0 0 24 24"><path fill="#fff" d="M6.6 10.8a15.1 15.1 0 0 0 6.6 6.6l2.2-2.2c.3-.3.7-.4 1-.2 1.1.4 2.3.6 3.6.6.6 0 1 .4 1 1V20c0 .6-.4 1-1 1A17 17 0 0 1 3 4c0-.6.4-1 1-1h3.5c.6 0 1 .4 1 1 0 1.3.2 2.5.6 3.6.1.3 0 .7-.2 1z"/></svg>
    123 456 7890
  </div>
  <div class="item" style="left:950px">
    <svg width="17" height="13" viewBox="0 0 24 18"><rect width="24" height="18" rx="2" fill="#fff"/><path d="M1 2l11 8 11-8" stroke="#3a1436" stroke-width="2" fill="none"/></svg>
    info@marlowcreek.com
  </div>
</header>

<nav class="abs site-nav">
  <div class="brand"><span class="dot"></span>Marlow Creek Stud</div>
  <div class="menu">
    <span class="active">HOME</span><span>STALLIONS</span><span>NEWS</span><span>SALES</span><span>GALLERY</span><span>ABOUT</span><span>CONTACT</span>
  </div>
</nav>

<section>
  <div class="photo hero-photo" role="img" aria-label="Bay horse cantering across a sunlit green paddock"></div>
  <div class="abs hero-disc"></div>
  <h1 class="abs hero-title" style="font-weight:400">INTER RELATION<br>BETWEEN<br>HORSE &amp; RIDER</h1>
  <svg class="abs hero-arrow" width="46" height="46" viewBox="0 0 46 46"><circle cx="23" cy="23" r="23" fill="#fff"/><path d="M14 23h17M24 16l7 7-7 7" stroke="#45193f" stroke-width="3" fill="none" stroke-linecap="round" stroke-linejoin="round"/></svg>
</section>

<section class="stallions">
  <h2 class="abs section-title" style="top:740px;font-weight:400">STALLIONS</h2>

  <div class="stallion-card">
    <div class="photo" style="left:78px;top:816px;background:linear-gradient(180deg,#6f9a4c 0%,#8a6a3e 60%,#b7b3a6 100%)" role="img" aria-label="Chestnut stallion standing side-on in a yard"></div>
    <div class="abs stallion-name" style="left:81px;top:1108px">Crown Of The Valley</div>
    <svg class="abs round-arrow" style="left:366px;top:1103px" viewBox="0 0 32 32"><circle cx="16" cy="16" r="14.5" fill="none" stroke="#45193f" stroke-width="2"/><path d="M9 16h13M17 11l5 5-5 5" stroke="#45193f" stroke-width="2.2" fill="none" stroke-linecap="round" stroke-linejoin="round"/></svg>
  </div>

  <div class="stallion-card">
    <div class="photo" style="left:438px;top:860px;background:linear-gradient(180deg,#c9b17a 0%,#3f5a2c 45%,#6a3d22 75%,#9a8d6c 100%)" role="img" aria-label="Bay stallion standing beside a hedge"></div>
    <div class="abs stallion-name" style="left:441px;top:1151px">Starlitmeridian</div>
    <svg class="abs round-arrow" style="left:728px;top:1146px" viewBox="0 0 32 32"><circle cx="16" cy="16" r="14.5" fill="none" stroke="#45193f" stroke-width="2"/><path d="M9 16h13M17 11l5 5-5 5" stroke="#45193f" stroke-width="2.2" fill="none" stroke-linecap="round" stroke-linejoin="round"/></svg>
  </div>

  <div class="stallion-card">
    <div class="photo" style="left:800px;top:816px;background:linear-gradient(180deg,#b9bfbe 0%,#6f7a6b 40%,#3a2418 70%,#a9a69d 100%)" role="img" aria-label="Dark bay stallion standing on a paved yard"></div>
    <div class="abs stallion-name" style="left:803px;top:1108px">Norse Harbour</div>
    <svg class="abs round-arrow" style="left:1090px;top:1103px" viewBox="0 0 32 32"><circle cx="16" cy="16" r="14.5" fill="none" stroke="#45193f" stroke-width="2"/><path d="M9 16h13M17 11l5 5-5 5" stroke="#45193f" stroke-width="2.2" fill="none" stroke-linecap="round" stroke-linejoin="round"/></svg>
  </div>

  <div class="abs slider-line"></div>
  <div class="abs slider-nav">
    <span><svg width="14" height="14" viewBox="0 0 14 14"><path d="M9 2L4 7l5 5" stroke="#333" stroke-width="2" fill="none"/></svg></span>
    <span><svg width="14" height="14" viewBox="0 0 14 14"><path d="M5 2l5 5-5 5" stroke="#333" stroke-width="2" fill="none"/></svg></span>
  </div>

  <svg class="abs" style="left:0;top:1268px" width="160" height="216" viewBox="0 0 160 216">
    <path d="M0 0 C60 40 110 110 150 216 L0 216 Z" fill="#e6dfe5"/>
    <path d="M0 40 C50 80 95 140 125 216 L0 216 Z" fill="#45193f"/>
  </svg>

  <p class="abs intro-quote">Lorem Ipsum is simply dummy text of the printing and typesetting industry.<br>Lorem Ipsum has been the industry's standard dummy text ever.</p>
</section>

<section class="news">
  <div class="photo news-photo" role="img" aria-label="Rider in dark jacket on a palomino horse wearing a bridle"></div>
  <h2 class="abs news-title" style="font-weight:400">LATEST NEWS</h2>
  <p class="abs news-lead">Lorem Ipsum is simply dummy text of the printing and typesetting industry. Lorem Ipsum has been the industry's standard dummy text ever</p>
  <p class="abs news-body">Lorem Ipsum is simply dummy text of the printing and typesetting industry. Lorem Ipsum has been the industry's standard dummy text ever since the 1500s, when an unknown printer took a galley of type and scrambled it to make a type specimen book. It has survived not only five centuries, but also the leap into electronic typesetting, remaining essentially unchanged. It was popularised in the 1960s with the release of Letraset sheets containing Lorem Ipsum passages, and more recently with desktop publishing software like Aldus PageMaker including versions of Lorem Ipsum.</p>
  <svg class="abs" style="left:1154px;top:1484px" width="46" height="481" viewBox="0 0 46 481">
    <path d="M0 0 H46 V481 H0 V345 L46 300 V290 L0 320 Z" fill="#45193f"/>
  </svg>
</section>

<section>
  <div class="photo banner" role="img" aria-label="Dark-toned photo of horses grazing behind a fence"></div>
  <p class="abs banner-text">LOREM IPSUM IS SIMPLY<br>DUMMY TEXT OF THE<br>PRINTING AND TYPESETTING.</p>
</section>

<section class="gallery">
  <h2 class="abs section-title" style="top:2482px;font-weight:400">GALLERY</h2>
  <div class="photo" style="left:78px;top:2546px;background:linear-gradient(180deg,#3d4a2e 0%,#6b8a3c 45%,#7a4a2a 65%,#6e9a44 100%)" role="img" aria-label="Herd of horses galloping across a paddock"></div>
  <div class="photo" style="left:432px;top:2579px;background:linear-gradient(180deg,#c7cdd0 0%,#9aa396 40%,#3a2a22 65%,#7f9b56 100%)" role="img" aria-label="Jockey riding a racehorse at gallop on grass"></div>
  <div class="photo" style="left:789px;top:2546px;background:linear-gradient(180deg,#3f7a35 0%,#5e8f3e 45%,#8a4f2a 70%,#7fae4c 100%)" role="img" aria-label="Bay horse standing by a wooden fence"></div>
  <div class="photo" style="left:78px;top:2838px;background:linear-gradient(180deg,#4a5a2e 0%,#b27a3a 45%,#c9a23a 75%,#d6b84a 100%)" role="img" aria-label="Chestnut horse trotting through golden grass"></div>
  <div class="photo" style="left:432px;top:2871px;background:linear-gradient(135deg,#8a5a3a 0%,#c08858 40%,#e8ddd4 75%,#f2eee9 100%)" role="img" aria-label="Woman standing beside a chestnut horse"></div>
  <div class="photo" style="left:789px;top:2838px;background:linear-gradient(180deg,#5a6e4a 0%,#7b8a6a 40%,#3a3530 65%,#9d9a90 100%)" role="img" aria-label="Handlers leading two horses along a fenced lane"></div>
</section>

<section>
  <div class="photo landscape" role="img" aria-label="Horses running through a meadow of white wildflowers below hills"></div>
</section>

<footer>
  <div class="abs footer"></div>
  <div class="abs subscribe">
    <span>Enter Your Email</span>
    <svg width="26" height="26" viewBox="0 0 24 24"><path d="M2 11L22 2 14 22 11 13z" fill="#45193f"/></svg>
  </div>
  <h3 class="abs subscribe-title" style="font-weight:400">SUBSCRIBE TO OUR NEWSLETTER</h3>

  <div class="abs footer-brand"><span class="dot"></span>Marlow Creek Stud</div>
  <p class="abs footer-about">Lorem Ipsum is simply dummy text of the printing and typesetting industry.</p>

  <h4 class="abs footer-heading" style="left:430px;font-weight:400">SITEMAP</h4>
  <ul class="abs sitemap" style="left:430px;top:3789px"><li>Home</li><li>Stallions</li><li>News</li><li>Sales</li></ul>
  <ul class="abs sitemap" style="left:633px;top:3789px"><li>Gallery</li><li>About</li><li>Contact</li><li>Privacy Policy</li></ul>

  <h4 class="abs footer-heading" style="left:803px;font-weight:400">CONTACT INFO</h4>
  <div class="abs contact-row" style="top:3796px">
    <svg width="16" height="20" viewBox="0 0 16 20"><path d="M8 0a8 8 0 0 0-8 8c0 6 8 12 8 12s8-6 8-12a8 8 0 0 0-8-8z" fill="#fff"/><circle cx="8" cy="8" r="3" fill="#45193f"/></svg>
    <span>Lorem Ipsum is simply dummy text of the printing and typesetting industry.</span>
  </div>
  <div class="abs contact-row" style="top:3862px">
    <svg width="16" height="16" viewBox="0 0 24 24"><path fill="#fff" d="M6.6 10.8a15.1 15.1 0 0 0 6.6 6.6l2.2-2.2c.3-.3.7-.4 1-.2 1.1.4 2.3.6 3.6.6.6 0 1 .4 1 1V20c0 .6-.4 1-1 1A17 17 0 0 1 3 4c0-.6.4-1 1-1h3.5c.6 0 1 .4 1 1 0 1.3.2 2.5.6 3.6.1.3 0 .7-.2 1z"/></svg>
    <span>123 456 7890</span>
  </div>
  <div class="abs contact-row" style="top:3900px">
    <svg width="17" height="13" viewBox="0 0 24 18"><rect width="24" height="18" rx="2" fill="#fff"/><path d="M1 2l11 8 11-8" stroke="#45193f" stroke-width="2" fill="none"/></svg>
    <span>info@marlowcreek.com</span>
  </div>

  <div class="abs copyright">2019 ©Marlow Creek Stud - All Rights Reserved.</div>
</footer>

</body>
</html>
```